Brookhaven Business Card

I would like to re-design my company business card. I have my main company logo (Brookhaven) which must remain unchanged and I also have a number of product brands which I would like to also show on the card in some way. The corporate company colors are Blue and Orange, see pantone colors on file. However, it is not necessary to use these colors thoroughout. I am ok with grey tones etc...

Target Market(s)

Trade Business

Industry/Entity Type

Furniture

Contact Information for Business Card

Needs to incorporate Brookhaven as the main Logo. The Torvel and Kandrel product brands within the company. These can be on the back of the card.

Font styles to use
Sans Serif

Colors
0355a3
f37122

Requirements
Must have
• Marco Velditch
• COO (Global)
• Brookhaven Pacific Holdings Inc. (4371)
• Level 3, 47 Harlow Street, Melbourne VIC 3000 Australia
• Tel: +61 3 9481 2736 Mobile: +61 427 586 204
• e-mail: marco@brookhaven-au.example
• web: www.brookhaven-au.example
Nice to have
• Should be a corporate
Should not have
• No images of furniture

```html
<!DOCTYPE html>
<html lang="en">
<head>
<meta charset="utf-8">
<title>Brookhaven Business Card</title>
<link href="https://fonts.googleapis.com/css2?family=Arimo:wght@400;700&display=swap" rel="stylesheet">
<style>
  :root {
    --brand-blue: #0355a3;
    --brand-blue-dark: #0a4488;
    --brand-orange: #f37122;
    --card-white: #fafafa;
    --ink: #1d1d1d;
    --stage: #3a3a3a;
  }
  * { margin: 0; padding: 0; box-sizing: border-box; }
  html, body { width: 1200px; height: 997px; overflow: hidden; }
  body {
    background: var(--stage);
    font-family: "Arimo", Arial, sans-serif;
    position: relative;
  }
  .card {
    position: absolute;
    width: 640px;
    height: 366px;
    border-radius: 22px;
    overflow: hidden;
    left: 280px;
    box-shadow: 0 10px 30px rgba(0,0,0,.45);
  }

  /* Back of card */
  .card-back {
    top: 72px;
    background: linear-gradient(160deg, #1a6cc0 0%, var(--brand-blue) 55%, var(--brand-blue-dark) 100%);
  }
  .card-back .divider { position: absolute; inset: 0; }
  .brand-lockup { position: absolute; display: flex; align-items: center; gap: 16px; }
  .brand-mark {
    width: 48px; height: 48px;
    background: var(--brand-orange);
    border-radius: 9px;
  }
  .brand-name { font-weight: 700; letter-spacing: -1px; }
  .card-back .brand-lockup { left: 150px; top: 140px; }
  .card-back .brand-name { font-size: 54px; color: #ffffff; }
  .product-badges {
    position: absolute;
    right: 28px; top: 86px;
    display: flex; gap: 6px;
  }
  .product-badge {
    width: 118px; height: 40px;
    background: #ffffff;
    clip-path: polygon(12% 0, 100% 0, 100% 100%, 0 100%);
    display: flex; align-items: center; justify-content: center;
    padding-left: 12px;
    font-weight: 700; font-size: 20px; color: var(--brand-blue);
  }

  /* Front of card */
  .card-front {
    top: 520px;
    background: linear-gradient(180deg, #ffffff 0%, #f1f1f1 100%);
  }
  .card-front .brand-lockup { left: 150px; top: 36px; }
  .card-front .brand-mark { width: 54px; height: 54px; }
  .card-front .brand-name { font-size: 50px; color: var(--brand-blue); }
  .card-front .art { position: absolute; inset: 0; }

  .holder { position: absolute; left: 36px; top: 150px; }
  .holder-name { font-weight: 700; font-size: 18px; color: var(--brand-blue); letter-spacing: .3px; }
  .holder-title { font-weight: 700; font-size: 15px; color: var(--brand-orange); margin-top: 2px; }

  .contact-list { position: absolute; left: 36px; top: 218px; list-style: none; }
  .contact-list li {
    display: flex; align-items: center; gap: 12px;
    font-size: 16px; color: var(--ink); height: 27px;
  }
  .contact-icon { width: 17px; height: 17px; flex: none; }

  .company { position: absolute; right: 36px; top: 128px; text-align: right; }
  .company-brand { font-weight: 700; font-size: 22px; color: var(--brand-blue); letter-spacing: -.5px; }
  .company-legal { font-weight: 700; font-size: 14px; color: var(--brand-orange); margin-top: 2px; }
  .company-address { font-size: 14px; color: var(--ink); line-height: 19px; margin-top: 2px; font-style: normal; }

  .web {
    position: absolute; right: 36px; bottom: 20px;
    font-weight: 700; font-size: 15px; color: #ffffff; letter-spacing: .3px;
  }
</style>
</head>
<body>

<section class="card card-back" aria-label="Back of business card">
  <svg class="divider" width="640" height="366" viewBox="0 0 640 366">
    <line x1="150" y1="366" x2="640" y2="118" stroke="#ffffff" stroke-width="2" opacity=".9"/>
  </svg>
  <div class="brand-lockup">
    <span class="brand-mark"></span>
    <span class="brand-name">Brookhaven</span>
  </div>
  <div class="product-badges">
    <div class="product-badge">Torvel</div>
    <div class="product-badge">Kandrel</div>
  </div>
</section>

<section class="card card-front" aria-label="Front of business card">
  <svg class="art" width="640" height="366" viewBox="0 0 640 366">
    <line x1="240" y1="158" x2="604" y2="112" stroke="var(--brand-blue)" stroke-width="2"/>
    <path d="M0 346 L300 346 C330 346 330 300 370 300 L640 300 L640 366 L0 366 Z" fill="var(--brand-blue)"/>
    <path d="M0 334 L292 334 C316 334 320 304 344 298 L354 298 C328 304 324 340 296 340 L0 340 Z" fill="var(--brand-orange)"/>
  </svg>

  <div class="brand-lockup">
    <span class="brand-mark"></span>
    <span class="brand-name">Brookhaven</span>
  </div>

  <div class="holder">
    <p class="holder-name">MARCO VELDITCH</p>
    <p class="holder-title">COO (GLOBAL)</p>
  </div>

  <ul class="contact-list">
    <li>
      <svg class="contact-icon" viewBox="0 0 20 20"><circle cx="10" cy="10" r="10" fill="var(--brand-blue)"/><path d="M6 6.5 Q10 4 14 6.5 L13 8.5 L11.5 8 L11.5 7 Q10 6.6 8.5 7 L8.5 8 L7 8.5 Z M6.5 10 h7 v4 h-7 Z" fill="#fff"/></svg>
      <span>+61 3 9481 2736</span>
    </li>
    <li>
      <svg class="contact-icon" viewBox="0 0 20 20"><circle cx="10" cy="10" r="10" fill="var(--brand-blue)"/><rect x="7" y="4.5" width="6" height="11" rx="1.2" fill="#fff"/><rect x="8" y="6" width="4" height="6" fill="var(--brand-blue)"/></svg>
      <span>+61 427 586 204</span>
    </li>
    <li>
      <svg class="contact-icon" viewBox="0 0 20 20"><circle cx="10" cy="10" r="10" fill="var(--brand-blue)"/><rect x="5" y="6.5" width="10" height="7" fill="#fff"/><path d="M5 6.5 L10 10.5 L15 6.5" stroke="var(--brand-blue)" stroke-width="1" fill="none"/></svg>
      <span>marco@brookhaven-au.example</span>
    </li>
  </ul>

  <div class="company">
    <p class="company-brand">Brookhaven</p>
    <p class="company-legal">Brookhaven Pacific Holdings Inc</p>
    <address class="company-address">Level 3, 47 Harlow Street<br>Melbourne VIC 3000 Australia</address>
  </div>

  <p class="web">www.brookhaven-au.example</p>
</section>

</body>
</html>
```